Fruit Juice packaging for Canada Market

We need label designs for our Fruit juice in PET form and we have 6 flavours ( tamarind, Blueberry, Passion Fruit+ Mango, Cucumis Melo+green tea, Mulberry, and Mango.
We need designs for packaging for all 6 listed fruits

1) Blueberry Juice labeling.
2) Tamarind Juice labeling.
3) Mulberry Juice labeling.
4) Passion fruit + Mango Juice labeling.
5) Cucumis Melo+green tea Juice labeling.
6) Mango Juice labeling.

A: PET bottle shape and dimensions:
- Dimensions: please refer to attachment name: VERUMO Bottle shape
- Bottle shape: Please refer to attachment name: BOTTLE SHAPE for the actual look of the bottle design.

B: Design Ideal: we want to have a look of fresh and juicy of real fruits since we are producing RAW juices. You can chose any taken photo of fruits on Pixelharbor. (http://www.pixelharbor-example.com/photos/blueberry?phrase=Blueberry&excludenudity=true&sort=best)

C: Fonts will be up to the designer choose, easy to read, neat and easy recognize

D: Label content needs to have followings: please refer to attachment VERUMO SAMPLE DESIGN for all needed information.
Main licence Company: HARLOWE Trading Inc.
Product Name: VERUMO
Product Name1 : Verumo Blueberry Juice (attached)
Flavor Name 1 : Blueberry
and
Product Name 2 : Verumo Tamarind Juice (attached)
Flavor Name 2: Tamarind
...and so on for the rest of juices

I want the design in English with editable Ai or PTS so that I can add shortly Vietnamese translation text as mandatory law in our current market-Vietnam. We will take care the translation for you.

Old labels are attached to give you an idea. Contents in the old will be pasted in your labels (nutrition facts, net weight, ingredient, direction of use... etc). you re-design to make it fresher and healthier.

On the label for 330ml PET bottle, (please see picture of sample bottle), decal dimension of L:17.5cm x H:12cm following phrase must be included:

- Made of Real Fruit Juice

- Direction of use: will be provided in Ai.
- Ingredients: will be provided in Ai.

- Production and Packaging under licence of
DORVEN INC., CANADA
452 Rue Fenwick Ouest, Quebec, CANADA.

- Importing, Producing and Distributing by PRELOM Ltd.,
- Km7, Lac Son town, Ho Chi Minh, Viet Nam.
- Made in Vietnam

- Nutrition Fact ( Canada label requirements)
- HALAL logo ( will be provided, show at front and on the back)
- ISO 22000:2005 logo (will be provided )
-Manufacturing date/Used by date: on the cap.
-Keep refrigerated for an even better taste.

(Somewhere in Front)

0% Cholesterol
Blueberry imports from CANADA. (for Blueberry Juice)
Delicious Tamarind from VIETNAM. ( for Tamarind juice)
Has HALAL logo at front ( see provided picture for reference)
picture of juice, fresh, wet fruits around the bottom bottle.
running juice from the juice at the bottom to the cap.

(P/S: the label packaging must meet the standard requirement for Canada)
Please request me for more info if needed.

VIETNAM and NORTH AMERICA

Pet

Serif
Sans Serif
Decorative
Script
Other font styles liked:
• Prefer to designers to chose on their design to make it looks match

Designer to choose colors to be used in the design.

• meet Canada Labeling requirement for imported products.
• Ai editable version is a must to allow us to add Vietnamese translation and movable objects on the packaging design after we add Vietnamese text.
• have done any packaging with Canadian customers with Nutrition Facts on.

```html
<!DOCTYPE html>
<html lang="en">
<head>
<meta charset="utf-8">
<title>VERUMO Fresh Juice Range</title>
<link rel="stylesheet" href="https://fonts.googleapis.com/css2?family=Questrial&display=swap">
<style>
  :root{
    --stage:#eef0f2;
    --cap:#ececec;
    --cap-ridge:#bdbdbd;
    --glass:#dfe8f0;
    --label:#ffffff;
    --brand-ink:#6a6a6a;
    --fresh-ink:#666666;
    --volume-ink:#c08a7a;
    --halal-ring:#2e7d3a;

    --cucumis-liquid:#eb9aa0; --cucumis-ink:#d6262d; --cucumis-fruit:#e0565e;
    --tamarind-liquid:#dccbb3; --tamarind-ink:#8e5a2c; --tamarind-fruit:#a7763f;
    --blueberry-liquid:#6a6aa8; --blueberry-ink:#5a5cb4; --blueberry-fruit:#5b5fa6;
    --mulberry-liquid:#7c7cc0; --mulberry-ink:#5a4a9c; --mulberry-fruit:#8a62b8;
    --passion-liquid:#e3d2a4; --passion-ink:#5a3d4c; --passion-fruit:#d9c63a;
    --mango-liquid:#e9e84c; --mango-ink:#f0a277; --mango-fruit:#f0c23a;
  }
  *{margin:0;padding:0;box-sizing:border-box}
  html,body{width:1200px;height:794px;overflow:hidden}
  body{background:var(--stage);font-family:"Questrial",sans-serif;position:relative}

  .bottle{position:absolute;top:104px;width:164px;height:610px}
  .bottle svg{position:absolute;inset:0;width:164px;height:610px}

  .label-text{position:absolute;left:0;width:164px;text-align:center}
  .brand{top:212px;font-size:25px;letter-spacing:1px;color:var(--brand-ink)}
  .fresh{top:326px;font-size:37px;line-height:1;color:var(--fresh-ink)}
  .flavour{top:366px;font-size:19px;line-height:22px;color:var(--ink)}
  .flavour .wide{letter-spacing:12px;padding-left:12px}
  .flavour .spaced{letter-spacing:7px;padding-left:7px}
  .volume{top:462px;font-size:9px;color:var(--volume-ink)}

  .cucumis{left:70px;--liquid:var(--cucumis-liquid);--ink:var(--cucumis-ink);--fruit:var(--cucumis-fruit)}
  .tamarind{left:248px;--liquid:var(--tamarind-liquid);--ink:var(--tamarind-ink);--fruit:var(--tamarind-fruit)}
  .blueberry{left:426px;--liquid:var(--blueberry-liquid);--ink:var(--blueberry-ink);--fruit:var(--blueberry-fruit)}
  .mulberry{left:606px;--liquid:var(--mulberry-liquid);--ink:var(--mulberry-ink);--fruit:var(--mulberry-fruit)}
  .passion{left:788px;--liquid:var(--passion-liquid);--ink:var(--passion-ink);--fruit:var(--passion-fruit)}
  .mango{left:970px;--liquid:var(--mango-liquid);--ink:var(--mango-ink);--fruit:var(--mango-fruit)}

  .liquid{fill:var(--liquid)}
  .glass{fill:var(--glass)}
  .label-band{fill:var(--label)}
  .fruit-splash{fill:var(--fruit);opacity:.85}
  .cap{fill:var(--cap)}
  .cap-ridge{stroke:var(--cap-ridge);stroke-width:2}
  .halal{fill:#fff;stroke:var(--halal-ring);stroke-width:2}
</style>
</head>
<body>

<!-- Bottle template repeated per flavour -->
<div class="bottle cucumis">
  <svg viewBox="0 0 164 610">
    <defs><clipPath id="shape-cucumis"><path d="M54 60H110L112 100C112 118 164 130 164 170V330C160 345 160 355 164 370V585C164 600 155 608 140 608H24C9 608 0 600 0 585V370C4 355 4 345 0 330V170C0 130 52 118 52 100Z"/></clipPath></defs>
    <g clip-path="url(#shape-cucumis)">
      <rect class="glass" x="0" y="55" width="164" height="60"/>
      <rect class="liquid" x="0" y="112" width="164" height="500"/>
      <rect class="label-band" x="0" y="150" width="164" height="410"/>
      <rect class="fruit-splash" x="0" y="478" width="164" height="82" role="img" aria-label="Cucumber slices, watermelon and green tea leaves in a pink juice splash"/>
    </g>
    <circle class="halal" cx="26" cy="530" r="11"/>
    <rect class="cap" x="38" y="0" width="88" height="52" rx="6"/>
    <line class="cap-ridge" x1="42" y1="40" x2="122" y2="40" stroke-dasharray="6 3"/>
    <rect class="cap" x="44" y="52" width="76" height="7" rx="2"/>
  </svg>
  <div class="label-text brand">VERUMO</div>
  <div class="label-text fresh">FRESH</div>
  <div class="label-text flavour">CUCUMISMELO<br>GREEN TEA<br><span class="wide">JUICE</span></div>
  <div class="label-text volume">330mL</div>
</div>

<div class="bottle tamarind">
  <svg viewBox="0 0 164 610">
    <defs><clipPath id="shape-tamarind"><path d="M54 60H110L112 100C112 118 164 130 164 170V330C160 345 160 355 164 370V585C164 600 155 608 140 608H24C9 608 0 600 0 585V370C4 355 4 345 0 330V170C0 130 52 118 52 100Z"/></clipPath></defs>
    <g clip-path="url(#shape-tamarind)">
      <rect class="glass" x="0" y="55" width="164" height="60"/>
      <rect class="liquid" x="0" y="112" width="164" height="500"/>
      <rect class="label-band" x="0" y="150" width="164" height="410"/>
      <rect class="fruit-splash" x="0" y="478" width="164" height="82" role="img" aria-label="Open tamarind pods in a golden juice splash"/>
    </g>
    <circle class="halal" cx="26" cy="530" r="11"/>
    <rect class="cap" x="38" y="0" width="88" height="52" rx="6"/>
    <line class="cap-ridge" x1="42" y1="40" x2="122" y2="40" stroke-dasharray="6 3"/>
    <rect class="cap" x="44" y="52" width="76" height="7" rx="2"/>
  </svg>
  <div class="label-text brand">VERUMO</div>
  <div class="label-text fresh">FRESH</div>
  <div class="label-text flavour"><span class="spaced">TAMARIND</span><br><span class="wide">JUICE</span></div>
  <div class="label-text volume">330mL</div>
</div>

<div class="bottle blueberry">
  <svg viewBox="0 0 164 610">
    <defs><clipPath id="shape-blueberry"><path d="M54 60H110L112 100C112 118 164 130 164 170V330C160 345 160 355 164 370V585C164 600 155 608 140 608H24C9 608 0 600 0 585V370C4 355 4 345 0 330V170C0 130 52 118 52 100Z"/></clipPath></defs>
    <g clip-path="url(#shape-blueberry)">
      <rect class="glass" x="0" y="55" width="164" height="60"/>
      <rect class="liquid" x="0" y="112" width="164" height="500"/>
      <rect class="label-band" x="0" y="150" width="164" height="410"/>
      <rect class="fruit-splash" x="0" y="478" width="164" height="82" role="img" aria-label="Fresh blueberries in a violet juice splash"/>
    </g>
    <circle class="halal" cx="26" cy="530" r="11"/>
    <rect class="cap" x="38" y="0" width="88" height="52" rx="6"/>
    <line class="cap-ridge" x1="42" y1="40" x2="122" y2="40" stroke-dasharray="6 3"/>
    <rect class="cap" x="44" y="52" width="76" height="7" rx="2"/>
  </svg>
  <div class="label-text brand">VERUMO</div>
  <div class="label-text fresh">FRESH</div>
  <div class="label-text flavour">BLUEBERRY<br><span class="wide">JUICE</span></div>
  <div class="label-text volume">330mL</div>
</div>

<div class="bottle mulberry">
  <svg viewBox="0 0 164 610">
    <defs><clipPath id="shape-mulberry"><path d="M54 60H110L112 100C112 118 164 130 164 170V330C160 345 160 355 164 370V585C164 600 155 608 140 608H24C9 608 0 600 0 585V370C4 355 4 345 0 330V170C0 130 52 118 52 100Z"/></clipPath></defs>
    <g clip-path="url(#shape-mulberry)">
      <rect class="glass" x="0" y="55" width="164" height="60"/>
      <rect class="liquid" x="0" y="112" width="164" height="500"/>
      <rect class="label-band" x="0" y="150" width="164" height="410"/>
      <rect class="fruit-splash" x="0" y="478" width="164" height="82" role="img" aria-label="Dark mulberries with a leaf in a purple juice splash"/>
    </g>
    <circle class="halal" cx="26" cy="530" r="11"/>
    <rect class="cap" x="38" y="0" width="88" height="52" rx="6"/>
    <line class="cap-ridge" x1="42" y1="40" x2="122" y2="40" stroke-dasharray="6 3"/>
    <rect class="cap" x="44" y="52" width="76" height="7" rx="2"/>
  </svg>
  <div class="label-text brand">VERUMO</div>
  <div class="label-text fresh">FRESH</div>
  <div class="label-text flavour">MULBERRY<br><span class="wide">JUICE</span></div>
  <div class="label-text volume">330mL</div>
</div>

<div class="bottle passion">
  <svg viewBox="0 0 164 610">
    <defs><clipPath id="shape-passion"><path d="M54 60H110L112 100C112 118 164 130 164 170V330C160 345 160 355 164 370V585C164 600 155 608 140 608H24C9 608 0 600 0 585V370C4 355 4 345 0 330V170C0 130 52 118 52 100Z"/></clipPath></defs>
    <g clip-path="url(#shape-passion)">
      <rect class="glass" x="0" y="55" width="164" height="60"/>
      <rect class="liquid" x="0" y="112" width="164" height="500"/>
      <rect class="label-band" x="0" y="150" width="164" height="410"/>
      <rect class="fruit-splash" x="0" y="478" width="164" height="82" role="img" aria-label="Halved passion fruit, mango and leaves in a yellow juice splash"/>
    </g>
    <circle class="halal" cx="26" cy="530" r="11"/>
    <rect class="cap" x="38" y="0" width="88" height="52" rx="6"/>
    <line class="cap-ridge" x1="42" y1="40" x2="122" y2="40" stroke-dasharray="6 3"/>
    <rect class="cap" x="44" y="52" width="76" height="7" rx="2"/>
  </svg>
  <div class="label-text brand">VERUMO</div>
  <div class="label-text fresh">FRESH</div>
  <div class="label-text flavour" style="font-size:17px">PASSION FRUIT<br><span class="spaced">&amp; MANGO</span><br><span class="wide">JUICE</span></div>
  <div class="label-text volume">330mL</div>
</div>

<div class="bottle mango">
  <svg viewBox="0 0 164 610">
    <defs><clipPath id="shape-mango"><path d="M54 60H110L112 100C112 118 164 130 164 170V330C160 345 160 355 164 370V585C164 600 155 608 140 608H24C9 608 0 600 0 585V370C4 355 4 345 0 330V170C0 130 52 118 52 100Z"/></clipPath></defs>
    <g clip-path="url(#shape-mango)">
      <rect class="glass" x="0" y="55" width="164" height="60"/>
      <rect class="liquid" x="0" y="112" width="164" height="500"/>
      <rect class="label-band" x="0" y="150" width="164" height="410"/>
      <rect class="fruit-splash" x="0" y="478" width="164" height="82" role="img" aria-label="Sliced ripe mango halves in a yellow juice splash"/>
    </g>
    <circle class="halal" cx="26" cy="530" r="11"/>
    <rect class="cap" x="38" y="0" width="88" height="52" rx="6"/>
    <line class="cap-ridge" x1="42" y1="40" x2="122" y2="40" stroke-dasharray="6 3"/>
    <rect class="cap" x="44" y="52" width="76" height="7" rx="2"/>
  </svg>
  <div class="label-text brand">VERUMO</div>
  <div class="label-text fresh">FRESH</div>
  <div class="label-text flavour"><span class="wide">MANGO</span><br><span class="wide">JUICE</span></div>
  <div class="label-text volume">330mL</div>
</div>

</body>
</html>
```